Business Card Design, including supply of raw art files plus a vector diagram of the zelvon logo and

We need the business card design for a company that is launching a new exciting product. The brief requires the submission of the following once the final design is chosen:

- business card layout including raw files
- a composite vector image file of the zelvon logo and tag line
- a standalone vector image file of the zelvon logo

The product will be launched as a customer engagement app.

It has 4 core modules which enables a person to do multiple things - book tours and activities, order takeaways, search for local deals and offers. A universal currency is at the heart of this product. When you use the app, you earn cashback rewards when shopping or buying at any of the merchant partners across the modules as . These rewards can then be used as full or part payment when buying goods or services at these merchant partners.

The business card must help us build the brand, communicate the benefit of the brand's key focus - the ability to earn and burn this universal cashback ccurrency - across the 4 modules - booking of tours and activities, ordering, searching for local deals and payment.

We would like the design to use the brand's blue colour the hex colour is: 00
Dark grey : 646464
Darker blue shadow: 058bdd
Main Blue: 0084ff

We need to translate this into a CMYK print or spot colour print.

Both print options to be supplied as separate files.

An example of the base concept we have in mind is attached for your reference.

The font used by the brand is Proxima Nova.

Note: the duration has been set as 2 days.

Industry/Entity Type

Business

Contact Information for Business Card

Carla Mendoza
Marketing
W: www.zelvon.example
M: + 61 400555123
T: +61 2 5550 1473
A: Suite 7, Level 2, 14-18 Harwick Street, Sydney, NSW, 2000, Australia

Font styles to use
Sans Serif

Requirements
Must have
• zelVon logo and tagline
• address details
• zelVon icons as supplied
Nice to have
• would like to have the option of a spot varnish layer over the logo and icons at the back of the card

```html
<!DOCTYPE html>
<html lang="en">
<head>
<meta charset="utf-8">
<title>zelVon business card</title>
<link rel="stylesheet" href="https://fonts.googleapis.com/css2?family=Source+Sans+3:wght@400;700&display=swap">
<style>
  :root {
    --backdrop: #3a3a3c;
    --card: #ffffff;
    --brand-blue: #2f86c8;
    --logo-blue: #3f97d6;
    --ink-grey: #4a4a4a;
    --text-grey: #555555;
  }
  * { margin: 0; padding: 0; box-sizing: border-box; }
  html, body { width: 1200px; height: 1200px; overflow: hidden; }
  body { background: var(--backdrop); position: relative; font-family: "Source Sans 3", sans-serif; }

  .card { position: absolute; left: 180px; width: 840px; height: 480px; background: var(--card); overflow: hidden; }
  .card--front { top: 96px; }
  .card--back { top: 624px; }

  .brand-mark { position: absolute; left: 187px; top: 124px; width: 132px; height: 132px; border-radius: 50%; background: var(--logo-blue); }
  .brand-name { position: absolute; left: 340px; top: 110px; font-weight: 400; font-size: 110px; line-height: 1; color: var(--ink-grey); }
  .brand-tagline { position: absolute; left: 346px; top: 222px; font-weight: 400; font-size: 26px; line-height: 1; color: var(--ink-grey); }

  .module-band { position: absolute; left: 0; top: 0; width: 840px; height: 480px; }

  .holder-name { position: absolute; left: 232px; top: 116px; font-weight: 700; font-size: 38px; line-height: 1; color: var(--brand-blue); letter-spacing: 0.3px; }
  .holder-role { position: absolute; left: 320px; top: 163px; font-size: 26px; line-height: 1; color: var(--text-grey); }

  .contact-icons { position: absolute; left: 0; top: 0; width: 840px; height: 480px; }
  .contact-line { position: absolute; left: 302px; font-size: 22px; line-height: 29px; color: var(--text-grey); }
  .contact-line--address { top: 238px; }
  .contact-line--phone { top: 313px; }
  .contact-line--web { top: 394px; }
</style>
</head>
<body>

<section class="card card--front">
  <div class="brand-mark"></div>
  <div class="brand-name">zelVon</div>
  <div class="brand-tagline">rewards you can spend</div>

  <svg class="module-band" viewBox="0 0 840 480" aria-label="Modules: tours, cashback, food ordering, deals">
    <polygon points="0,350 654,350 628,449 0,449" fill="var(--brand-blue)"/>
    <g fill="#fff">
      <rect x="186" y="380" width="68" height="44" rx="4"/>
      <rect x="204" y="372" width="26" height="12" rx="3"/>
      <circle cx="220" cy="402" r="14" fill="var(--brand-blue)"/>
      <circle cx="220" cy="402" r="10"/>
      <circle cx="247" cy="386" r="2.5" fill="var(--brand-blue)"/>
    </g>
    <rect x="276" y="376" width="4" height="42" fill="#fff"/>
    <g fill="none" stroke="#fff" stroke-width="5">
      <path d="M298 384 a22 22 0 0 1 22 -10"/>
      <path d="M346 414 a22 22 0 0 1 -22 10"/>
    </g>
    <polygon points="290,380 304,374 302,392" fill="#fff"/>
    <polygon points="352,418 338,424 340,406" fill="#fff"/>
    <circle cx="322" cy="399" r="13" fill="#fff"/>
    <text x="322" y="406" text-anchor="middle" font-family="Source Sans 3, sans-serif" font-weight="700" font-size="19" fill="var(--brand-blue)">$</text>
    <rect x="366" y="376" width="4" height="42" fill="#fff"/>
    <g stroke="#fff" stroke-width="4" stroke-linecap="round">
      <line x1="388" y1="382" x2="424" y2="424"/>
      <line x1="416" y1="388" x2="386" y2="424"/>
      <line x1="386" y1="372" x2="394" y2="382"/>
      <line x1="392" y1="370" x2="398" y2="378"/>
    </g>
    <ellipse cx="420" cy="380" rx="7" ry="11" transform="rotate(40 420 380)" fill="#fff"/>
    <rect x="456" y="376" width="4" height="42" fill="#fff"/>
    <path d="M480 396 L505 371 L534 371 L534 398 L509 423 Z" fill="#fff"/>
    <circle cx="524" cy="382" r="4" fill="var(--brand-blue)"/>
  </svg>
</section>

<section class="card card--back">
  <div class="holder-name">CARLA MENDOZA</div>
  <div class="holder-role">marketing</div>

  <svg class="contact-icons" viewBox="0 0 840 480" aria-hidden="true">
    <g fill="var(--brand-blue)">
      <circle cx="253" cy="258" r="21"/>
      <circle cx="253" cy="332" r="21"/>
      <circle cx="253" cy="407" r="21"/>
    </g>
    <path d="M253 269 L247 256 a7 7 0 1 1 12 0 Z" fill="#fff"/>
    <circle cx="253" cy="252" r="2.5" fill="var(--brand-blue)"/>
    <rect x="247" y="321" width="12" height="22" rx="2" fill="none" stroke="#fff" stroke-width="2"/>
    <rect x="249" y="325" width="8" height="13" fill="#fff"/>
    <g fill="none" stroke="#fff" stroke-width="1.6">
      <circle cx="253" cy="407" r="9"/>
      <ellipse cx="253" cy="407" rx="4" ry="9"/>
      <line x1="244" y1="407" x2="262" y2="407"/>
      <line x1="246" y1="402" x2="260" y2="402"/>
      <line x1="246" y1="412" x2="260" y2="412"/>
    </g>
  </svg>

  <div class="contact-line contact-line--address">Suite 7, Level 2, 14-18 Harwick Street,<br>Sydney, NSW, 2000, Australia</div>
  <div class="contact-line contact-line--phone">+ 61 400555123<br>+61 2 5550 1473</div>
  <div class="contact-line contact-line--web">W: www.zelvon.example</div>
</section>

</body>
</html>
```